Harborne Cellarbook: the premier wine registry - (need business cards)

We have a logo designed, and now we need business cards for our 3 founders. Harborne Cellarbook is the premier wine registry for weddings. I am envisioning the wine glass with the heart in it as our signature symbol. (FYI- on the red background file, only use the part that has the red background; the brown colors are not relevant)

```html
<!DOCTYPE html>
<html lang="en">
<head>
<meta charset="utf-8">
<title>Harborne Cellarbook – Founder Business Card</title>
<link href="https://fonts.googleapis.com/css2?family=Parisienne&family=Alegreya+SC:wght@400&display=swap" rel="stylesheet">
<style>
  :root {
    --card-wine: #93234a;
    --title-blush: #f7d6df;
    --role-blush: #f3cdd8;
    --contact-cream: #fbe9ee;
  }
  html, body {
    margin: 0;
    padding: 0;
    width: 1200px;
    height: 707px;
    overflow: hidden;
    background: var(--card-wine);
  }
  .business-card {
    position: relative;
    width: 1200px;
    height: 707px;
    background: var(--card-wine);
    overflow: hidden;
  }
  .founder-name {
    position: absolute;
    left: 68px;
    top: 52px;
    margin: 0;
    font-family: "Parisienne", cursive;
    font-weight: 400;
    font-size: 88px;
    line-height: 1.2;
    color: var(--title-blush);
    letter-spacing: 1px;
  }
  .founder-role {
    position: absolute;
    left: 72px;
    top: 210px;
    margin: 0;
    font-family: "Alegreya SC", serif;
    font-size: 31px;
    letter-spacing: 2.5px;
    color: var(--role-blush);
    text-transform: uppercase;
  }
  .contact-list {
    position: absolute;
    right: 68px;
    top: 356px;
    margin: 0;
    padding: 0;
    list-style: none;
    text-align: right;
    font-family: "Alegreya SC", serif;
    font-size: 28px;
    line-height: 48.6px;
    letter-spacing: 1.6px;
    color: var(--contact-cream);
  }
</style>
</head>
<body>
  <main class="business-card">
    <h1 class="founder-name">Founder's Name</h1>
    <p class="founder-role">Founder</p>
    <ul class="contact-list">
      <li class="contact-mobile">Mobile: +123 456 7890</li>
      <li class="contact-landline">Landline: +123 456 7890</li>
      <li class="contact-address">Office Address: 123 Street, City, ST 12345</li>
      <li class="contact-email">Email: hello@hcellarbook.com</li>
      <li class="contact-website">Official Website: www.harbornecellarbook.com</li>
      <li class="contact-social">Instagram @harbornecellarbook</li>
    </ul>
  </main>
</body>
</html>
```